Option Sheet

We need a one page option sheet with a left to right reading of the five options. It should be a one sheet, multiple colors and definitive separations between options This is used in a sales consultation. Backround or colors not in option need to have the follow RGB value (5 red, 20 green, 63 blue)

We added a smaller text file, please change that point

Target Market(s)

Divorce

Industry/Entity Type

Legal

Requirements
Must have
• 1) All five options left to right
• 2)language included in sheet

```html
<!DOCTYPE html>
<html lang="en">
<head>
<meta charset="utf-8">
<title>Divorce – Five Options</title>
<link href="https://fonts.googleapis.com/css2?family=Oswald:wght@400;500&family=Source+Sans+3:wght@400;600;700&display=swap" rel="stylesheet">
<style>
  :root{
    --sheet-bg:#b8cccc;
    --header-bg:#f4f5f6;
    --title-cyan:#17b0d6;
    --subtitle-blue:#2e5aa6;
    --swoosh-blue:#3a55a4;
    --text:#3a3a3c;
    --card:#ffffff;
    --opt1:#9cc93a;
    --opt2:#fdc321;
    --opt3:#f58a1f;
    --opt4:#1db3d9;
    --opt5:#3b5ba8;
  }
  *{box-sizing:border-box;margin:0;padding:0}
  html,body{width:1200px;height:866px;overflow:hidden}
  body{background:var(--sheet-bg);font-family:"Source Sans 3",Arial,sans-serif;color:var(--text);position:relative}
  .sheet{position:absolute;inset:0;background:linear-gradient(180deg,#c6d6d6 0%,var(--sheet-bg) 100%)}
  .header-art{position:absolute;left:0;top:0;width:1200px;height:180px}
  .title{position:absolute;top:22px;left:0;width:100%;text-align:center;font-family:"Oswald",Arial,sans-serif;font-weight:500;font-size:62px;letter-spacing:3px;color:var(--title-cyan);line-height:1}
  .subtitle{position:absolute;top:98px;left:0;width:100%;text-align:center;font-family:"Oswald",Arial,sans-serif;font-weight:400;font-size:24px;color:var(--subtitle-blue);line-height:1}
  .footer-band{position:absolute;left:0;right:0;bottom:8px;height:9px;background:var(--swoosh-blue)}
  .options{position:absolute;left:14px;top:214px;width:1172px;height:596px;display:flex;gap:8px}
  .option{position:relative;flex:0 0 228px;height:100%}
  .option-tab{position:absolute;left:16px;right:16px;top:0;height:58px;border-radius:16px 16px 0 0;color:#fff;text-align:center;padding-top:9px;z-index:2}
  .option-tab .number{display:block;font-weight:700;font-size:17px;line-height:1.1}
  .option-tab .name{display:block;font-weight:400;font-size:15px;line-height:1.2}
  .option-card{position:absolute;left:0;right:0;top:28px;bottom:0;background:linear-gradient(180deg,#f3f4f5 0%,var(--card) 45%);border-radius:20px;overflow:hidden;box-shadow:0 2px 5px rgba(0,0,0,.12);padding:44px 12px 24px}
  .option-card::after{content:"";position:absolute;left:0;right:0;bottom:0;height:13px;background:var(--accent)}
  .section-title{text-align:center;font-weight:700;font-size:14px;color:var(--accent);margin-bottom:4px;letter-spacing:.2px}
  .points{list-style:none;font-size:13.2px;line-height:1.25}
  .points li{padding-left:8px;text-indent:-8px;margin-bottom:6px}
  .points li::before{content:"• "}
  .divider{border:0;border-top:1px dashed var(--accent);margin:10px 6px 14px;opacity:.8}
  .option--1{--accent:var(--opt1)} .option--1 .option-tab{background:var(--opt1)}
  .option--2{--accent:var(--opt2)} .option--2 .option-tab{background:var(--opt2)}
  .option--3{--accent:var(--opt3)} .option--3 .option-tab{background:var(--opt3)}
  .option--4{--accent:var(--opt4)} .option--4 .option-tab{background:var(--opt4)}
  .option--5{--accent:var(--opt5)} .option--5 .option-tab{background:var(--opt5)}
  .option--5 .divider{margin-top:22px}
</style>
</head>
<body>
<div class="sheet">
  <svg class="header-art" viewBox="0 0 1200 180" aria-hidden="true">
    <path d="M0 0H1200V70C900 150 500 190 0 98Z" fill="var(--header-bg)"/>
    <path d="M0 98C500 190 900 150 1200 70" fill="none" stroke="var(--title-cyan)" stroke-width="7"/>
    <path d="M0 104C500 198 900 158 1200 78" fill="none" stroke="var(--swoosh-blue)" stroke-width="6"/>
  </svg>
  <h1 class="title">DIVORCE</h1>
  <p class="subtitle">FIVE OPTIONS</p>

  <div class="options">
    <section class="option option--1">
      <div class="option-tab"><span class="number">OPTION #1</span><span class="name">Do Nothing</span></div>
      <div class="option-card">
        <h3 class="section-title">ADVANTAGES:</h3>
        <ul class="points"><li>Stay married</li><li>No life Changes</li></ul>
        <hr class="divider">
        <h3 class="section-title">DISADVANTAGES:</h3>
        <ul class="points">
          <li>Remain unhappy, depressed, anxious</li><li>Feel unsafe</li>
          <li>Money and assets may disappear</li>
          <li>Spouse may threaten to leave and/or divorce you</li>
          <li>May cause children to be confused, distressed</li>
          <li>What is going to change?</li>
        </ul>
      </div>
    </section>

    <section class="option option--2">
      <div class="option-tab"><span class="number">OPTION #2</span><span class="name">Go to Counseling</span></div>
      <div class="option-card">
        <h3 class="section-title">ADVANTAGES:</h3>
        <ul class="points"><li>Reconcile marriage</li><li>Help make a better life</li></ul>
        <hr class="divider">
        <h3 class="section-title">DISADVANTAGES:</h3>
        <ul class="points">
          <li>Past issues are highlighted and may drudge up old wounds</li>
          <li>It may just clarify the reasons you need to separate and/or divorce</li>
          <li>There is no quick fix for any situation and BOTH parties must be invested and willing to participate</li>
          <li>Bringing a third party into the marriage may cause more confusion and possible distrust</li>
        </ul>
      </div>
    </section>

    <section class="option option--3">
      <div class="option-tab"><span class="number">OPTION #3</span><span class="name">Do it Yourself</span></div>
      <div class="option-card">
        <h3 class="section-title">ADVANTAGES:</h3>
        <ul class="points"><li>No attorney fees</li></ul>
        <hr class="divider">
        <h3 class="section-title">DISADVANTAGES:</h3>
        <ul class="points">
          <li>People often find that what is “fair,” may in fact, not be truly fair</li>
          <li>Often times, people do not know the risks</li>
          <li>Complicated legal system</li>
          <li>Unsure how to complete the necessary paperwork and meet the deadlines</li>
          <li>You are too emotional and may be unable to remain clear-headed</li>
          <li>It can be very stressful</li>
        </ul>
      </div>
    </section>

    <section class="option option--4">
      <div class="option-tab"><span class="number">OPTION #4</span><span class="name">Limited Representation</span></div>
      <div class="option-card">
        <h3 class="section-title">ADVANTAGES:</h3>
        <ul class="points"><li>Balance between going alone and our limited involvement in the case</li></ul>
        <hr class="divider">
        <h3 class="section-title">DISADVANTAGES:</h3>
        <ul class="points">
          <li>Our terms may not benefit from our legal knowledge</li>
          <li>The legal consequences of your legal documents will not be explained to you so that you can formulate a plan for handling the rest of your case.</li>
          <li>Your spouse or other parties may cause your legal fees to increase significantly without action on your part</li>
        </ul>
      </div>
    </section>

    <section class="option option--5">
      <div class="option-tab"><span class="number">OPTION #5</span><span class="name">Hire Us</span></div>
      <div class="option-card">
        <h3 class="section-title">ADVANTAGES:</h3>
        <ul class="points">
          <li>Provide peace of mind</li>
          <li>Often saves you money in the long run</li>
          <li>Can stop problems before they start and advise how actions /events may impact your case</li>
          <li>May be able to come to a settlement agreement sooner</li>
          <li>Lessen the emotional stress of one of the worst things that can happen to a person</li>
          <li>Inform you of your rights and what you are entitled to</li>
          <li>Save you time and energy</li>
          <li>Gain the full benefits of our experience</li>
          <li>Provide a shoulder to lean on and a sounding board</li>
        </ul>
        <hr class="divider">
        <h3 class="section-title">DISADVANTAGES:</h3>
        <ul class="points"><li>Cost</li></ul>
      </div>
    </section>
  </div>

  <div class="footer-band"></div>
</div>
</body>
</html>
```